Orthopedic Arm Surgeon Brochure

Bifold modern design. I will supply the text, my photo, and photos of my textbooks. Prefer colors in the greens, blues, greys. For more information visit LimbForwardClinic.com Please feel free to e-mail me with any questions. Current brochure attached; I want to modernize this, get rid of frames, and change the text.

Target Market(s)

High-end market

Colors
3176b5
33a6d7
33b8a4
abd036
876aae
b768aa

Requirements
Must have
• Beautiful finishes
Should not have
• Bright reds, yellows, oranges that emit fear

```html
<!DOCTYPE html>
<html lang="en">
<head>
<meta charset="utf-8">
<title>Hand &amp; Arm Conditions Brochure</title>
<link rel="stylesheet" href="https://fonts.googleapis.com/css2?family=Gelasio:wght@400;700&display=swap">
<style>
  :root {
    --backdrop: #e4e4e6;
    --paper: #fafafa;
    --ink: #1c1c1c;
    --rule: #111111;
    --photo-light: #f3eeee;
    --photo-skin: #e2b8ad;
    --photo-key: #3a3940;
    --photo-shadow: #1f1e24;
    --fold: rgba(0, 0, 0, 0.07);
  }
  * { box-sizing: border-box; margin: 0; padding: 0; }
  html, body {
    width: 1200px;
    height: 1200px;
    overflow: hidden;
    background: var(--backdrop);
    font-family: "Gelasio", Georgia, serif;
    color: var(--ink);
  }
  .brochure-spread {
    position: absolute;
    left: 50px;
    top: 215px;
    width: 1100px;
    height: 770px;
    overflow: hidden;
    background: var(--paper);
    display: grid;
    grid-template-columns: 360px 380px 360px;
    grid-template-rows: 770px;
    box-shadow: 0 18px 40px rgba(0, 0, 0, 0.12);
  }
  .text-panel {
    height: 770px;
    padding: 44px 34px 36px 40px;
    display: flex;
    flex-direction: column;
  }
  .condition-title {
    font-weight: 700;
    font-size: 20px;
    line-height: 1.2;
    margin-bottom: 10px;
  }
  .condition-body,
  .closing-note {
    font-size: 14.5px;
    line-height: 1.45;
  }
  .section-rule {
    border: none;
    height: 3px;
    background: var(--rule);
    width: 78%;
    margin: 24px 0;
    flex-shrink: 0;
  }
  .feature-photo {
    position: relative;
    height: 770px;
    background:
      radial-gradient(ellipse 40% 18% at 70% 52%, var(--photo-skin) 0%, rgba(226,184,173,0) 100%),
      radial-gradient(ellipse 35% 14% at 60% 28%, rgba(226,184,173,0.8) 0%, rgba(226,184,173,0) 100%),
      linear-gradient(150deg, var(--photo-light) 0%, #e9dfe2 30%, var(--photo-key) 62%, var(--photo-shadow) 78%, #d9d7d8 100%);
  }
  .feature-photo::after {
    content: "";
    position: absolute;
    top: 0;
    bottom: 0;
    left: 50%;
    width: 2px;
    background: var(--fold);
  }
</style>
</head>
<body>
  <main class="brochure-spread">
    <section class="text-panel panel-left">
      <h2 class="condition-title">Carpal Tunnel<br>Syndrome</h2>
      <p class="condition-body">Carpal Tunnel Syndrome occurs when the main/median nerve to the hand gets pinched at the wrist. This leads to fingers feeling “numb”, “asleep”, “cold”, like they “lack circulation” or have “pins and needles” in them. Carpal tunnel syndrome is usually worst at night or upon awakening. If you wake up at night with your hand numb or painfully asleep, and have to “shake it out” to get relief, you’ve probably got carpal tunnel syndrome. Symptoms also often occur with gripping, such as when driving, writing or holding books, cell phones or tools.</p>
      <hr class="section-rule">
      <h2 class="condition-title">Cubital Tunnel<br>Syndrome</h2>
      <p class="condition-body">Cubital tunnel syndrome occurs when the funny bone (ulnar) nerve gets pinched at the elbow. This leads to tingling and numbness of the small finger when the elbow is bent, usually at night or when talking on the phone. Numbness may also occur when the elbow is placed on a hard surface.</p>
    </section>

    <div class="feature-photo" role="img" aria-label="Close-up photograph of hands typing on a laptop keyboard"></div>

    <section class="text-panel panel-right">
      <h2 class="condition-title">Trigger Finger</h2>
      <p class="condition-body">Trigger finger occurs when the tendon that moves the finger gets pinched in its tunnel. This causes the finger to get stuck or stiff, which is often worse in the morning. This catching or locking can be quite painful. Grip may also cause pain. The finger may occasionally get stuck straight and be difficult to bend.</p>
      <hr class="section-rule">
      <h2 class="condition-title">Wrist Pain</h2>
      <p class="condition-body">Wrist pain may have many causes and the diagnosis is best made by a fellowship-trained Hand Surgeon. The most common cause is DeQuervain’s tendinitis, which causes pain on the thumb side of the wrist. This occurs when the tendons to the thumb and wrist get pinched in their tunnel. Pain is usually worse with lifting and gripping.</p>
      <hr class="section-rule">
      <p class="closing-note">To see more information and video about everything please go to :<br>www.LimbForwardClinic.com</p>
    </section>
  </main>
</body>
</html>
```